Email footer for a cafe

The task is to design an email footer for a new start up cafe business. The logo has been designed, but we would like a professional email footer to sign off on all emails.

The email footer should :
1. look professional and competent
2. be clean and easy to read
3. the email must have the ability to optimise / adjust across the bottom of the email depending on the device being used to read the email
4. the design may stretch across the entire bottom of the email, but this is not mandatory
5. it must incorporate the logo and the details as listed below.
6. For any additional lines / dividers that a designer might choose to incorporate into the email footer, our preference is to match the colour of the logo.

The logo is attached. The logo details are:

The CMYK for the logo is C0 M50 Y100 K0 in font BankGothic Lt BT - Light
The CMKY for the text is C75 M68 Y67 K89 in font AvantGarde Bk BT - Book

The details to be included in the email footer are:

Ted Varro
Founder
0417 283 614
pelvar@brookfieldkitchenqx.com
Unit 6, 14 Malvory Crescent
Tembly KLW 5213

Have fun and thank you in advance for choosing to work on our job.

Reason: Thank you to everyone who has submitted their designs for an email footer. Looking at the designs most have been designed horizontally. Could I please also see some designs where all the elements are under each other in a stacked format. I have attached 2 images which I have grabbed from the internet to be used as an example.

```html
<!DOCTYPE html>
<html lang="en">
<head>
<meta charset="utf-8">
<title>Brookfield Kitchen – Email Footer</title>
<link rel="stylesheet" href="https://fonts.googleapis.com/css2?family=Questrial&display=swap">
<style>
  :root {
    --stage: #5e5e5e;
    --paper: #fffaf3;
    --brand-orange: #f7941d;
    --ink: #161616;
    --white: #ffffff;
  }
  * { margin: 0; padding: 0; box-sizing: border-box; }
  html, body {
    width: 1200px;
    height: 1000px;
    overflow: hidden;
    background: var(--stage);
  }
  .canvas {
    position: relative;
    width: 1200px;
    height: 1000px;
  }
  .email-footer {
    position: absolute;
    left: 325px;
    top: 300px;
    width: 198px;
    height: 298px;
    background: var(--paper);
    border: 1px solid var(--brand-orange);
    font-family: "Questrial", "Century Gothic", sans-serif;
    color: var(--ink);
  }
  .sign-off {
    position: absolute;
    left: 18px;
    top: 24px;
    font-size: 9px;
    line-height: 11px;
  }
  .name-line {
    position: absolute;
    left: 18px;
    top: 40px;
    height: 14px;
    display: flex;
    align-items: center;
    white-space: nowrap;
  }
  .person-name {
    font-size: 12px;
    font-variant: small-caps;
    color: var(--brand-orange);
    letter-spacing: 1px;
  }
  .divider-bar {
    width: 1.5px;
    height: 12px;
    background: var(--ink);
    margin: 0 6px;
  }
  .role {
    font-size: 9px;
  }
  .company-line {
    position: absolute;
    left: 18px;
    top: 57px;
    font-size: 10px;
    line-height: 12px;
    font-variant: small-caps;
    color: var(--brand-orange);
    letter-spacing: 1px;
    white-space: nowrap;
  }
  .contact-list {
    position: absolute;
    left: 17px;
    top: 76px;
    list-style: none;
    font-size: 8.5px;
    line-height: 11px;
  }
  .contact-item {
    display: flex;
    align-items: flex-start;
    margin-bottom: 7px;
    white-space: nowrap;
  }
  .contact-icon {
    width: 10px;
    height: 10px;
    margin-right: 5px;
    flex-shrink: 0;
  }
  .brand-mark {
    position: absolute;
    left: 0;
    top: 196px;
    width: 198px;
    display: flex;
    justify-content: center;
    align-items: center;
    gap: 7px;
    font-family: "Questrial", "Century Gothic", sans-serif;
    color: var(--brand-orange);
  }
  .brand-dot {
    width: 9px;
    height: 9px;
    border-radius: 50%;
    background: var(--brand-orange);
  }
  .brand-name {
    font-size: 17px;
    line-height: 22px;
    letter-spacing: 0.5px;
    white-space: nowrap;
  }
  .link-row {
    position: absolute;
    left: 17px;
    top: 268px;
    width: 164px;
    display: flex;
    justify-content: space-between;
    align-items: center;
  }
  .link-icon {
    width: 15px;
    height: 15px;
  }
</style>
</head>
<body>
<main class="canvas">
  <section class="email-footer" aria-label="Email signature">
    <p class="sign-off">Best Regards,</p>
    <div class="name-line">
      <span class="person-name">Ted Varro</span>
      <span class="divider-bar"></span>
      <span class="role">Founder</span>
    </div>
    <p class="company-line">Brookfield Kitchen</p>

    <ul class="contact-list">
      <li class="contact-item">
        <svg class="contact-icon" viewBox="0 0 10 10" aria-hidden="true">
          <rect width="10" height="10" rx="2" fill="var(--brand-orange)"/>
          <path d="M5 8.5 C3.2 6.2 2.6 5.2 2.6 4 a2.4 2.4 0 0 1 4.8 0 c0 1.2-0.6 2.2-2.4 4.5z" fill="var(--white)"/>
          <circle cx="5" cy="4" r="0.9" fill="var(--brand-orange)"/>
        </svg>
        <span>Unit 6, 14 Malvory Crescent<br>Tembly KLW 5213</span>
      </li>
      <li class="contact-item">
        <svg class="contact-icon" viewBox="0 0 10 10" aria-hidden="true">
          <rect width="10" height="10" rx="2" fill="var(--brand-orange)"/>
          <path d="M3 2.2 L4.3 2 L4.8 3.8 L4 4.4 C4.4 5.4 5 6 5.9 6.4 L6.5 5.6 L8.1 6.1 L8 7.5 C5 7.8 2.4 5.2 3 2.2z" fill="var(--white)"/>
        </svg>
        <span>0417 283 614</span>
      </li>
      <li class="contact-item">
        <svg class="contact-icon" viewBox="0 0 10 10" aria-hidden="true">
          <rect width="10" height="10" rx="2" fill="var(--brand-orange)"/>
          <rect x="2" y="3" width="6" height="4.2" fill="var(--white)"/>
          <path d="M2 3 L5 5.4 L8 3" fill="none" stroke="var(--brand-orange)" stroke-width="0.7"/>
        </svg>
        <span>pelvar@brookfieldkitchenqx.com</span>
      </li>
    </ul>

    <div class="brand-mark">
      <span class="brand-dot"></span>
      <span class="brand-name">Brookfield Kitchen</span>
    </div>

    <nav class="link-row" aria-label="Contact links">
      <svg class="link-icon" viewBox="0 0 15 15" aria-label="Email">
        <rect x="1" y="3.5" width="13" height="8.5" rx="1" fill="var(--brand-orange)"/>
        <path d="M1.5 4 L7.5 8.5 L13.5 4" fill="none" stroke="var(--paper)" stroke-width="1"/>
      </svg>
      <svg class="link-icon" viewBox="0 0 15 15" aria-label="Website">
        <g fill="none" stroke="var(--brand-orange)" stroke-width="1.2">
          <circle cx="7.5" cy="7.5" r="6"/>
          <ellipse cx="7.5" cy="7.5" rx="2.6" ry="6"/>
          <line x1="1.5" y1="7.5" x2="13.5" y2="7.5"/>
          <line x1="2.5" y1="4.5" x2="12.5" y2="4.5"/>
          <line x1="2.5" y1="10.5" x2="12.5" y2="10.5"/>
        </g>
      </svg>
      <svg class="link-icon" viewBox="0 0 15 15" aria-label="Location">
        <path d="M7.5 14 C4.5 10 3.2 8 3.2 5.6 a4.3 4.3 0 0 1 8.6 0 c0 2.4-1.3 4.4-4.3 8.4z" fill="var(--brand-orange)"/>
        <circle cx="7.5" cy="5.6" r="1.7" fill="var(--paper)"/>
      </svg>
      <svg class="link-icon" viewBox="0 0 15 15" aria-label="Share">
        <g fill="var(--brand-orange)">
          <circle cx="11.5" cy="3.5" r="2.2"/>
          <circle cx="3.5" cy="7.5" r="2.2"/>
          <circle cx="11.5" cy="11.5" r="2.2"/>
        </g>
        <path d="M11.5 3.5 L3.5 7.5 L11.5 11.5" fill="none" stroke="var(--brand-orange)" stroke-width="1.2"/>
      </svg>
      <svg class="link-icon" viewBox="0 0 15 15" aria-label="Message">
        <path d="M2 2.5 H13 a1 1 0 0 1 1 1 V10 a1 1 0 0 1-1 1 H6 L3 13.5 V11 H2 a1 1 0 0 1-1-1 V3.5 a1 1 0 0 1 1-1z" fill="var(--brand-orange)"/>
        <g fill="var(--paper)">
          <circle cx="4.5" cy="6.8" r="0.9"/>
          <circle cx="7.5" cy="6.8" r="0.9"/>
          <circle cx="10.5" cy="6.8" r="0.9"/>
        </g>
      </svg>
      <svg class="link-icon" viewBox="0 0 15 15" aria-label="Call">
        <path d="M3.5 1.5 L5.8 1.2 L6.8 4.6 L5.3 5.7 C6 7.4 7.4 8.9 9.2 9.7 L10.3 8.2 L13.6 9.2 L13.3 11.6 C8 12.4 2.5 7 3.5 1.5z" fill="var(--brand-orange)"/>
      </svg>
    </nav>
  </section>
</main>
</body>
</html>
```